PrairieKite - New Website Design

Create a professional Shopify website for the hottest trend; a box of school supplies subscription box business called PrairieKite. Wexelo.com is an easy to use website builder.
Please see fernwhistle.com; lunapebble.com; quietmeadowfolk.com; and tovinjar.com for the concept I am after. The business has not been launched yet, I am currently in the pre-launch stage using a specialized landing page website, and so the time scale for developing my professional looking Shopify website is up to 1-2 weeks.
The webpage should have a fun feel and should match the style of the company logo at lunapebble.com. The pages to include are 'Home', 'About us' and 'Get Started'
Thank you and good luck!

```html
<!DOCTYPE html>
<html lang="en">
<head>
<meta charset="utf-8">
<title>PrairieKite — Home</title>
<link href="https://fonts.googleapis.com/css2?family=Abril+Fatface&family=Open+Sans:ital,wght@0,400;0,600;1,400&display=swap" rel="stylesheet">
<style>
:root{
  --brand:#c0385a;
  --ink:#111111;
  --text:#555555;
  --muted:#777777;
  --rule:#222222;
  --footer-bg:#efefef;
  --white:#ffffff;
  --black:#000000;
}
*{box-sizing:border-box;margin:0;padding:0}
html,body{width:1200px;height:3072px;overflow:hidden;background:var(--white)}
body{position:relative;font-family:"Open Sans",Arial,sans-serif;color:var(--ink)}
.abs{position:absolute}
.serif{font-family:"Abril Fatface",Georgia,serif}

/* top bar */
.topbar{left:0;top:0;width:1200px;height:33px;background:var(--black);color:var(--white);
  font-size:11px;font-weight:600;text-align:center;line-height:33px;letter-spacing:.3px}
.topbar svg{position:absolute;top:10px}

/* header */
.logo{left:131px;top:58px;font-size:37px;color:var(--brand);line-height:48px}
.nav{top:72px;font-size:12.5px;color:var(--ink)}
.nav.active{color:var(--brand);border-bottom:1px solid var(--brand);padding-bottom:1px}

/* hero */
.hero{left:0;top:129px;width:1200px;height:485px;
  background:linear-gradient(100deg,#d9a43a 0%,#5a5f66 22%,#3f4449 50%,#55595e 75%,#9bb33a 100%)}
.hero-arrow{top:363px}
.hero-card{left:422px;top:190px;width:356px;height:363px;background:var(--white);padding:10px}
.hero-card-inner{width:100%;height:100%;border:1.5px solid var(--rule);text-align:center;position:relative}
.hero-title{position:absolute;top:60px;width:100%;font-size:31px;font-family:"Abril Fatface",Georgia,serif;font-weight:400;color:#222}
.hero-rule{position:absolute;top:124px;left:136px;width:64px;height:1.5px;background:var(--rule)}
.hero-text{position:absolute;top:152px;left:40px;right:40px;font-style:italic;font-size:13px;line-height:24px;color:var(--muted)}
.hero-cta{position:absolute;top:265px;left:0;width:100%;font-size:13px;color:#222;letter-spacing:.4px}
.hero-cta::before,.hero-cta::after{content:"";position:absolute;top:9px;width:80px;height:1.5px;background:var(--rule)}
.hero-cta::before{left:16px}.hero-cta::after{right:16px}

/* section heads */
.section-title{left:0;width:1200px;text-align:center;font-size:22px;font-weight:600;letter-spacing:.4px}
.section-rule{left:562px;width:76px;height:1.5px;background:var(--rule)}
.intro{left:133px;top:763px;width:934px;text-align:center;font-size:13.5px;line-height:19px;color:var(--muted)}

/* products */
.product-img{top:1020px;width:297px;height:223px}
.product-name{top:1256px;width:297px;text-align:center;font-size:13px;letter-spacing:.3px;color:#222}

/* band */
.band{left:0;top:1352px;width:1200px;height:401px;
  background:linear-gradient(90deg,#d98aa8 0%,#e9e0cf 30%,#f1ebe0 55%,#dfe3ea 80%,#b79ad0 100%)}
.band-card{left:422px;top:1500px;width:356px;height:106px;background:var(--white);padding:13px}
.band-card-inner{width:100%;height:100%;border:1.5px solid var(--rule);text-align:center;
  font-family:"Abril Fatface",Georgia,serif;font-size:29px;line-height:77px;color:#222}

/* offers */
.offer{top:1915px;height:237px;display:flex;align-items:center;justify-content:center;
  font-family:"Abril Fatface",Georgia,serif;font-size:31px;color:var(--white)}

/* instagram */
.insta{top:2314px;width:195px;height:176px}

/* footer */
.footer{left:0;top:2591px;width:1200px;height:481px;background:var(--footer-bg)}
.footer-logo{left:426px;top:2550px;width:348px;height:88px;background:var(--white);padding:6px}
.footer-logo-inner{width:100%;height:100%;border:1.5px solid var(--rule);text-align:center;
  font-family:"Abril Fatface",Georgia,serif;font-size:38px;line-height:73px;color:var(--brand)}
.col-title{top:2706px;font-family:"Abril Fatface",Georgia,serif;font-size:15px;color:#222}
.col-rule{top:2740px;width:297px;height:1px;background:#444}
.links{left:133px;top:2756px;list-style:none;font-size:11px;line-height:21px;color:#555}
.links li::before{content:"› ";}
.about-text,.news-text{top:2748px;width:297px;font-size:11px;line-height:17px;color:#555}
.email{left:770px;top:2796px;width:201px;height:35px;background:var(--white);font-size:10.5px;color:#999;line-height:35px;padding-left:16px}
.email-btn{left:971px;top:2796px;width:96px;height:35px;background:#1f1f1f;color:var(--white);font-size:12px;line-height:35px;text-align:center}
.copyright{left:0;top:2896px;width:1200px;text-align:center;font-size:11px;color:#555}
.pay{top:2946px;width:30px;height:18px;background:#8a8a8a;border-radius:2px}
.social{top:3000px;width:18px;height:18px;border-radius:50%;background:#555}
</style>
</head>
<body>

<div class="abs topbar">
  <svg style="left:132px" width="12" height="13" viewBox="0 0 12 13"><circle cx="6" cy="3.5" r="3" fill="#fff"/><path d="M0 13c0-4 2.5-6 6-6s6 2 6 6z" fill="#fff"/></svg>
  FREE SHIPPING ON ORDERS OVER $100
  <svg style="left:1054px" width="13" height="13" viewBox="0 0 13 13"><circle cx="5" cy="5" r="4" stroke="#fff" stroke-width="2" fill="none"/><line x1="8" y1="8" x2="12" y2="12" stroke="#fff" stroke-width="2"/></svg>
</div>

<div class="abs logo serif">PrairieKite</div>
<span class="abs nav active" style="left:736px">Home</span>
<span class="abs nav" style="left:800px">About Us</span>
<span class="abs nav" style="left:883px">Subscribe</span>
<span class="abs nav" style="left:969px">FAQ</span>
<span class="abs nav" style="left:1023px">Contact</span>

<div class="abs hero" role="img" aria-label="School supplies on a chalkboard: colored pencils, calculator, paper clips, scissors, push pins and a green apple"></div>
<svg class="abs hero-arrow" style="left:8px" width="12" height="16" viewBox="0 0 12 16"><path d="M9 2 3 8l6 6" stroke="#fff" stroke-width="2" fill="none"/></svg>
<svg class="abs hero-arrow" style="left:1180px" width="12" height="16" viewBox="0 0 12 16"><path d="M3 2l6 6-6 6" stroke="#fff" stroke-width="2" fill="none"/></svg>
<div class="abs hero-card"><div class="hero-card-inner">
  <h1 class="hero-title">Etiam quis</h1>
  <div class="hero-rule"></div>
  <p class="hero-text">Suspendisse gravida ornare erat sed pulvinar. Vestibulum luctus ex in egestas fringilla.</p>
  <div class="hero-cta">SUBSCRIBE NOW</div>
</div></div>

<h2 class="abs section-title" style="top:686px">MAURIS BIBENDUM</h2>
<p class="abs intro">Nulla in lorem at massa pellentesque posuere. Nulla tristique posuere molestie. Aliquam erat volutpat. Etiam quis aliquet risus. Duis ornare erat eget magna dapibus, in accumsan quam pharetra. Nam tempus, quam in bibendum vulputate, sapien dolor viverra nisl, vitae euismod elit turpis et nulla. Aliquam erat volutpat. Pellentesque blandit lacus eget nunc faucibus, et tincidunt eros viverra. Phasellus consequat sagittis nisi suscipit feugiat. Cras eget leo sed nunc hendrerit ultricies eu at nisl.</p>

<h2 class="abs section-title" style="top:930px">OUR PRODUCTS</h2>
<div class="abs section-rule" style="top:987px"></div>
<div class="abs product-img" style="left:133px;background:linear-gradient(135deg,#2f8a5a,#e8c74a 50%,#d44a8c)" role="img" aria-label="Notebook with pencils and rulers"></div>
<div class="abs product-img" style="left:451px;background:linear-gradient(135deg,#6d8a4a,#c8344a 50%,#7a4e36)" role="img" aria-label="Backpack stuffed with school books and an apple"></div>
<div class="abs product-img" style="left:770px;background:linear-gradient(135deg,#8a6a50,#efe8d8 50%,#d24040)" role="img" aria-label="Notebook, compass and scissors on a wooden desk"></div>
<div class="abs product-name" style="left:133px">PRAESENT IACULIS FAUCIBUS</div>
<div class="abs product-name" style="left:451px">MAECENAS CONSEQUAT</div>
<div class="abs product-name" style="left:770px">FUSCE EGET</div>

<div class="abs band" role="img" aria-label="Flat lay of pencils, scissors, binder clips, sharpeners and a ruler on light wood"></div>
<div class="abs band-card"><div class="band-card-inner">Aliquam erat</div></div>

<h2 class="abs section-title" style="top:1823px">SPECIAL OFFERS</h2>
<div class="abs section-rule" style="top:1880px"></div>
<div class="abs offer" style="left:133px;width:451px;background:linear-gradient(120deg,#2a3fa0,#d8402e 40%,#e8b830 65%,#7a38a8)" role="img" aria-label="Colorful paper clips and pencils">Aliquam consectetur</div>
<div class="abs offer" style="left:614px;width:453px;background:linear-gradient(120deg,#8a7a78,#b08a8a 45%,#6a8ab0)" role="img" aria-label="Notebook with paper clips and colored pencils">Proin eget</div>

<h2 class="abs section-title" style="top:2225px">INSTAGRAM</h2>
<div class="abs section-rule" style="top:2280px"></div>
<div class="abs insta" style="left:0;background:linear-gradient(135deg,#d8a050,#3a7ab8)" role="img" aria-label="School supplies flat lay"></div>
<div class="abs insta" style="left:201px;background:linear-gradient(135deg,#3a8a8a,#2a4ab0)" role="img" aria-label="Blue backpack by a chalkboard"></div>
<div class="abs insta" style="left:402px;background:linear-gradient(135deg,#e8e0d8,#c8a0a0)" role="img" aria-label="Shopping cart full of supplies"></div>
<div class="abs insta" style="left:603px;background:linear-gradient(135deg,#f0f0f0,#e8c040)" role="img" aria-label="Yellow backpack with supplies"></div>
<div class="abs insta" style="left:804px;background:linear-gradient(90deg,#e84a3a,#e8c03a,#3aa84a,#3a6ae8)" role="img" aria-label="Row of colored pencils"></div>
<div class="abs insta" style="left:1005px;background:linear-gradient(135deg,#d84a8a,#3a8ad8)" role="img" aria-label="Tablet with colored pencils"></div>

<div class="abs footer"></div>
<div class="abs footer-logo"><div class="footer-logo-inner">PrairieKite</div></div>

<div class="abs col-title" style="left:133px">Links</div>
<div class="abs col-rule" style="left:133px"></div>
<ul class="abs links"><li>Home</li><li>About Us</li><li>Subscribe</li><li>FAQ</li><li>Contact</li></ul>

<div class="abs col-title" style="left:453px;top:2694px">About</div>
<div class="abs col-rule" style="left:453px;top:2728px"></div>
<p class="abs about-text" style="left:453px;top:2740px">Proin placerat dapibus gravida. In tristique tristique nulla eget hendrerit. Maecenas vel tortor accumsan quam varius imperdiet vel eget elit. Aenean facilisis tincidunt lectus, id dictum nisi luctus eget. Vivamus efficitur ex condimentum, malesuada eros eget, feugiat nibh.</p>

<div class="abs col-title" style="left:770px">Newsletter</div>
<div class="abs col-rule" style="left:770px"></div>
<p class="abs news-text" style="left:770px">Maecenas vel tortor accumsan quam varius imperdiet vel eget elit. Aenean facilisis tincidunt lectus.</p>
<div class="abs email">Email Address</div>
<div class="abs email-btn">SUBSCRIBE</div>

<div class="abs copyright">Copyright © 2017 PrairieKite. All rights reserved.</div>
<div class="abs pay" style="left:526px"></div>
<div class="abs pay" style="left:566px"></div>
<div class="abs pay" style="left:606px"></div>
<div class="abs pay" style="left:646px"></div>
<div class="abs social" style="left:531px"></div>
<div class="abs social" style="left:571px"></div>
<div class="abs social" style="left:611px"></div>
<div class="abs social" style="left:651px"></div>

</body>
</html>
```